Brochure Design Project

11x17 flat...folds to 8.5x11
full color
Utilize customers images and web content to create sleek brochure showcasing customers capabilities.
www.brightvaleworks.com
Logo added to uploads.
Reason: Customer is out of town.

```html
<!DOCTYPE html>
<html lang="en">
<head>
<meta charset="utf-8">
<title>Brightvale Works Brochure</title>
<link href="https://fonts.googleapis.com/css2?family=Open+Sans:wght@400;600&family=Parisienne&display=swap" rel="stylesheet">
<style>
  :root{
    --bg:#000;
    --text:#fff;
    --accent:#27d0e0;
    --yellow:#f2f200;
    --bullet:#b8c43a;
    --frame:#8a8a3a;
    --brand:#3fb0c8;
    --footer:#1b1b1b;
    --link:#3fc7e8;
  }
  *{margin:0;padding:0;box-sizing:border-box}
  html,body{width:1200px;height:776px;overflow:hidden;background:var(--bg)}
  body{position:relative;font-family:"Open Sans",Arial,sans-serif;color:var(--text)}
  .abs{position:absolute}
  .line{display:block;white-space:nowrap}
  .brand{display:flex;align-items:center;gap:8px;font-weight:600;font-size:19px;letter-spacing:1px;color:var(--brand);text-transform:uppercase}
  .brand-mark{width:14px;height:14px;background:var(--brand)}
  .intro{font-size:14px;line-height:19px}
  .intro .lead{font-size:26px;font-weight:600;line-height:1}
  .script{font-family:"Parisienne",cursive;color:var(--accent);font-size:24px;line-height:1;font-weight:400}
  .script .hi{color:var(--yellow)}
  .services{list-style:none;font-size:14.3px}
  .services li{height:23.5px;display:flex;align-items:center}
  .services li::before{content:"";width:6px;height:6px;border-radius:50%;background:var(--bullet);margin:0 7px 0 2px}
  .product-copy{font-size:14.3px;line-height:19.7px}
  .photo{border:2px solid var(--frame)}
  .footer{left:0;top:737px;width:1200px;height:39px;background:var(--footer);font-size:10px;display:flex;align-items:center;padding-left:23px;white-space:nowrap}
  .footer a{color:var(--link);text-decoration:none}
</style>
</head>
<body>
  <div class="abs brand" style="left:14px;top:32px"><span class="brand-mark"></span>Brightvale Works</div>
  <div class="abs brand" style="left:968px;top:32px"><span class="brand-mark"></span>Brightvale Works</div>

  <p class="abs intro" style="left:13px;top:96px">
    <span class="line"><span class="lead">We</span> have over 36 years of experience in design production. Our unparalleled services have</span>
    <span class="line">been requested both locally and nationally. Please visit our website to see our works.</span>
  </p>

  <h2 class="abs script" style="left:14px;top:156px">Our Services</h2>
  <ul class="abs services" style="left:20px;top:182px">
    <li>Interactive Activities</li>
    <li>Design Production</li>
    <li>Event Planner Cleveland</li>
    <li>Event Planning Businesses</li>
    <li>Event Planning Firms</li>
    <li>Event Planning Companies</li>
    <li>Corporate Event Planner</li>
    <li>Wedding and Event Planning</li>
    <li>Party Decorations</li>
    <li>Wedding Planner Ohio</li>
    <li>Bounce House Rental</li>
    <li>Wedding Planner Cleveland</li>
  </ul>

  <h2 class="abs script" style="left:20px;top:512px">New Event Photo Product- <span class="hi">Photo Canvas Frame</span></h2>
  <p class="abs product-copy" style="left:23px;top:547px">
    <span class="line">Brightvale Works is proud to introduce the newest</span>
    <span class="line">photo concept on the market, Custom Photo Canvas'</span>
    <span class="line">printed on site. Each guest will take a photo, and with</span>
    <span class="line">our high capacity printers, we will print directly on</span>
    <span class="line">canvas, frame it and the guests will walk away with a</span>
    <span class="line">fantastic canvas photo, to cherish for years to come.</span>
  </p>
  <div class="abs photo" role="img" aria-label="Family portrait printed on canvas" style="left:410px;top:552px;width:149px;height:117px;background:linear-gradient(160deg,#c9d7dc,#d9b89a 60%,#a88566)"></div>

  <p class="abs intro" style="left:636px;top:96px">
    <span class="line"><span class="lead">We</span> have created many awesome work. Here arte some samples. Please visit our</span>
    <span class="line">website to see our works.</span>
  </p>
  <h2 class="abs script" style="left:636px;top:158px">Design Portfolio</h2>

  <div class="abs photo" role="img" aria-label="Guest photo composited with a dinosaur scene" style="left:635px;top:204px;width:117px;height:60px;background:linear-gradient(135deg,#4d6a3a,#8a9a6a)"></div>
  <div class="abs photo" role="img" aria-label="Guest photo composited in a space rover scene" style="left:775px;top:204px;width:117px;height:60px;background:linear-gradient(135deg,#1a2c5a,#6a7a9a)"></div>
  <div class="abs photo" role="img" aria-label="Guest photo composited with an underwater dolphin scene" style="left:915px;top:204px;width:117px;height:60px;background:linear-gradient(135deg,#1a5a9a,#4aa0d0)"></div>
  <div class="abs photo" role="img" aria-label="Guest photo composited in a space rover scene" style="left:1055px;top:204px;width:117px;height:60px;background:linear-gradient(135deg,#1a2c5a,#7a7a8a)"></div>

  <div class="abs photo" role="img" aria-label="Guest photo in front of a Paris landmark" style="left:635px;top:279px;width:86px;height:118px;background:linear-gradient(180deg,#4a7ac8,#8aaad8 60%,#6a5a4a)"></div>
  <div class="abs photo" role="img" aria-label="Guest on a racing magazine cover" style="left:727px;top:279px;width:84px;height:118px;background:linear-gradient(180deg,#c83a2a,#8a6a5a)"></div>
  <div class="abs photo" role="img" aria-label="Custom caricature bobblehead poster" style="left:817px;top:279px;width:85px;height:118px;background:linear-gradient(180deg,#3a4a3a,#6a6a4a)"></div>
  <div class="abs photo" role="img" aria-label="Guest on a racing magazine cover" style="left:908px;top:279px;width:84px;height:118px;background:linear-gradient(180deg,#c83a2a,#8a6a5a)"></div>
  <div class="abs photo" role="img" aria-label="Custom caricature figures poster" style="left:998px;top:279px;width:85px;height:118px;background:linear-gradient(180deg,#2a3a3a,#5a5a4a)"></div>
  <div class="abs photo" role="img" aria-label="Custom caricature figures poster" style="left:1088px;top:279px;width:84px;height:118px;background:linear-gradient(180deg,#2a3a3a,#5a5a4a)"></div>

  <div class="abs photo" role="img" aria-label="Personalized phone cases, stationery, pens and bookmarks" style="left:638px;top:426px;width:213px;height:286px;background:linear-gradient(160deg,#f4f4f4,#e8d8ec 50%,#d8f0e8)"></div>
  <div class="abs photo" role="img" aria-label="Personalized flip book promotion" style="left:874px;top:426px;width:143px;height:194px;background:linear-gradient(160deg,#f2ece0,#d8c8a8)"></div>
  <div class="abs photo" role="img" aria-label="Guests on a sports magazine cover" style="left:1034px;top:426px;width:138px;height:194px;background:linear-gradient(180deg,#f0f0f0,#c83a3a 30%,#8a4a3a)"></div>
  <div class="abs photo" role="img" aria-label="Personalized photo license plates" style="left:874px;top:625px;width:196px;height:87px;background:linear-gradient(135deg,#2a2a2a,#7a6a5a)"></div>
  <div class="abs photo" role="img" aria-label="Engraved photo pendants and keychains" style="left:1076px;top:625px;width:96px;height:87px;background:linear-gradient(135deg,#1a1a1a,#8a8a8a)"></div>

  <div class="abs footer">Visit us at&nbsp;<a href="#">http://www.brightvaleworks.com/</a>, For general enquery mail us at&nbsp;<a href="#">info@brightvaleworks.com</a>&nbsp;and for sales enquery mail us at&nbsp;<a href="#">sales@brightvaleworks.com</a>, call us at toll free no. Cleveland-<a href="#">(888) 555-0147</a>, Florida-<a href="#">(888) 555-0147</a></div>
</body>
</html>
```